Move the hackers to Wordpress

Yep, we want to move https://www.brasslantern.com/ to Wordpress. It'll make it easier to update and add content. I'd like mostly the same look, but I'm not stuck with it.
Updates

DO NOT RESPOND OUTSIDE OF PIXEL BAZAAR OR CONTACT US DIRECTLY.

Industry/Entity Type

Computer Security

Coding

Coded - Design and coding required

Font styles to use
Sans Serif

Colors
ec1f27

Requirements
Must have
• What I do want is:
• 1. Similar look to the existing site
• 2. Needs to work on one of the Wordpress hosting sites. I do NOT want to run my own Wordpress server.
• 3. Keep the animation in the top panel.
• 4. Mobile support
• The rest can be changed as needed.
Nice to have
• I like the transitions when the "services" panel shows up. Not stuck on it, but it is a nice touch.

```html
<!DOCTYPE html>
<html lang="en">
<head>
<meta charset="utf-8">
<title>Brass Lantern – Information Security</title>
<link href="https://fonts.googleapis.com/css2?family=Poppins:wght@300;400;500;600&display=swap" rel="stylesheet">
<style>
:root{
  --red:#ec1f27;
  --ink:#1b1b1b;
  --text:#333;
  --muted:#777;
  --light:#f1f1f1;
  --card-line:#e2e2e2;
  --dark:#111214;
  --white:#fff;
}
*{box-sizing:border-box;margin:0;padding:0}
html,body{width:1200px;height:3965px;overflow:hidden}
body{font-family:"Poppins",sans-serif;color:var(--text);background:var(--white);position:relative}
.abs{position:absolute}

/* header */
.site-header{position:absolute;left:0;top:0;width:1200px;height:104px;background:var(--white);z-index:3}
.brand{position:absolute;left:161px;top:32px;display:flex;align-items:center;gap:10px}
.brand-mark{width:30px;height:30px;background:var(--red)}
.brand-name{font-size:21px;font-weight:500;color:var(--red);letter-spacing:2px;line-height:1}
.brand-tag{font-size:7px;letter-spacing:2.3px;color:var(--red);margin-top:3px;font-weight:500}
.main-nav{position:absolute;left:472px;top:44px;display:flex;gap:50px;font-size:13px;font-weight:500;color:var(--ink)}
.header-phone{position:absolute;left:870px;top:40px;display:flex;align-items:center;gap:8px;color:var(--red);font-size:19px;font-weight:500}

/* hero */
.hero{position:absolute;left:0;top:104px;width:1200px;height:660px;overflow:hidden}
.hero-image{position:absolute;inset:0;background:radial-gradient(ellipse at 78% 40%,#3e4f63 0%,#1c2532 30%,#0b0f15 65%,#05070a 100%)}
.hero-title{position:absolute;left:161px;top:214px;color:var(--white);font-size:35px;font-weight:500;line-height:44px}
.hero-cut{position:absolute;left:0;top:0}

/* what we do */
.section-title{font-size:30px;font-weight:400;color:var(--ink);letter-spacing:.5px}
.rule{width:64px;height:3px;background:var(--red)}
.what-title{left:161px;top:842px}
.what-rule{left:161px;top:916px}
.lead{color:var(--red);font-size:21px;line-height:29px;font-weight:400}
.what-lead{left:161px;top:940px;width:440px}
.body-copy{font-size:11.5px;line-height:22px;color:#444}
.what-copy{left:161px;top:1012px;width:440px}
.what-frame{left:675px;top:815px;width:370px;height:392px;background:var(--red)}
.what-image{left:663px;top:803px;width:372px;height:392px;background:radial-gradient(circle at 50% 45%,#9fc2e6 0%,#4c6b93 22%,#233346 50%,#0d1219 100%)}

/* services */
.services-bg{left:0;top:1290px;width:1200px;height:1080px}
.services-title{left:0;top:1448px;width:1200px;text-align:center}
.services-rule{left:568px;top:1500px}
.card{position:absolute;width:278px;height:323px;background:var(--white);border:1px solid var(--card-line);text-align:center;padding:0 26px}
.card.raised{box-shadow:0 6px 18px rgba(0,0,0,.13)}
.card svg{margin-top:38px}
.card h3{font-size:14.5px;font-weight:400;color:var(--ink);line-height:24px;margin-top:16px}
.card p{font-size:10.5px;line-height:20px;color:#444;margin-top:14px;height:80px;overflow:hidden}
.card .more{display:block;margin-top:12px;font-size:11px;font-weight:600;color:var(--red)}

/* about us */
.about-title{left:161px;top:2626px}
.about-rule{left:161px;top:2684px}
.about-lead{left:161px;top:2716px;width:290px;font-size:21px;line-height:33px}
.about-frame{left:501px;top:2533px;width:546px;height:323px;background:var(--red)}
.about-image{left:489px;top:2545px;width:546px;height:323px;background:radial-gradient(ellipse at 35% 35%,#6d7787 0%,#3a414d 40%,#16191e 100%)}
.play{left:706px;top:2663px}

/* testimonials */
.testi-bg{left:0;top:3040px;width:1200px;height:660px}
.testi-title{left:0;top:3166px;width:1200px;text-align:center}
.testi-rule{left:568px;top:3218px}
.quote{position:absolute;width:326px;height:192px;background:var(--white);border:1px solid var(--card-line);padding:26px 28px}
.quote.raised{box-shadow:0 6px 18px rgba(0,0,0,.15);top:3282px}
.quote p{font-size:12px;line-height:20px;font-style:italic;color:#bbb}
.quote.raised p{color:#333}
.quote .who{position:absolute;left:28px;top:116px;display:flex;align-items:center;gap:14px}
.avatar{width:62px;height:62px;border-radius:50%;background:linear-gradient(#d9cfc6,#a99c91)}
.who-name{font-size:11px;color:var(--red)}
.stars{font-size:11px;color:#bbb;letter-spacing:2px}

/* footer */
.footer{left:0;top:3640px;width:1200px;height:325px}
.foot-brand{left:0;top:3700px;width:1200px;display:flex;justify-content:center;align-items:center;gap:14px}
.foot-brand .brand-mark{width:44px;height:44px}
.foot-brand .brand-name{font-size:31px;letter-spacing:4px}
.foot-brand .brand-tag{font-size:9px;letter-spacing:4px}
.foot-contact{left:0;top:3790px;width:1200px;text-align:center;color:var(--white);font-size:15px}
.foot-contact span{margin:0 8px}
.foot-legal{left:0;top:3836px;width:1200px;text-align:center;color:#bbb;font-size:9.5px}
.socials{left:0;top:3882px;width:1200px;display:flex;justify-content:center;gap:14px}
.socials i{width:22px;height:22px;border-radius:50%;background:#2a2b2e;display:block}
</style>
</head>
<body>

<header class="site-header">
  <div class="brand">
    <div class="brand-mark"></div>
    <div><div class="brand-name">BRASS LANTERN</div><div class="brand-tag">INFORMATION SECURITY</div></div>
  </div>
  <nav class="main-nav"><span>SERVICES</span><span>BLOG</span><span>PRESS</span><span>CONTACT</span></nav>
  <div class="header-phone">
    <svg width="20" height="20" viewBox="0 0 24 24" fill="none" stroke="#ec1f27" stroke-width="2"><path d="M5 3h4l2 5-3 2a11 11 0 0 0 6 6l2-3 5 2v4a2 2 0 0 1-2 2A18 18 0 0 1 3 5a2 2 0 0 1 2-2z"/></svg>
    +1.555.014.2270
  </div>
</header>

<section class="hero">
  <div class="hero-image" role="img" aria-label="Close-up of a human eye over streams of binary code"></div>
  <h1 class="hero-title">Offensive Services<br>From Offensive Minds</h1>
  <svg class="hero-cut" width="1200" height="660" viewBox="0 0 1200 660"><polygon points="0,500 360,615 1200,520 1200,660 0,660" fill="#fff"/></svg>
</section>

<h2 class="abs section-title what-title">WHAT WE DO</h2>
<div class="abs rule what-rule"></div>
<p class="abs lead what-lead">We are an information security company focusing on real world threats.</p>
<p class="abs body-copy what-copy">Brass Lantern is an information security consulting company that concentrates on the latest threats to organizations today. We perform in-depth analysis, determine organization/business risk, and find the vulnerabilities before the bad guys do. Our team includes internationally renowned experts who have been featured in international news outlets and conferences, including The Daily Ledger, The Capital Courier, a Harbor News Documentary.</p>
<div class="abs what-frame"></div>
<div class="abs what-image" role="img" aria-label="Digital eye with glowing scan rings"></div>

<svg class="abs services-bg" viewBox="0 0 1200 1080"><polygon points="0,80 420,0 1200,150 1200,980 700,1080 0,940" fill="#f1f1f1"/></svg>
<h2 class="abs section-title services-title">SERVICES</h2>
<div class="abs rule services-rule"></div>

<div class="card" style="left:161px;top:1546px">
  <svg width="50" height="56" viewBox="0 0 50 56" fill="none" stroke="#ec1f27" stroke-width="3"><path d="M6 3h26l12 12v38H6z"/><path d="M14 24h22M14 32h22M14 40h22"/></svg>
  <h3>Internal Pivot Assessment<br>and Post Exploitation</h3>
  <p>We start as a low privilege user and attempt to move through the network in an attempt to access the data the matters to you. This is a simulation of a rogue</p>
  <span class="more">READ MORE</span>
</div>
<div class="card raised" style="left:460px;top:1546px">
  <svg width="60" height="56" viewBox="0 0 60 56" fill="none" stroke="#ec1f27" stroke-width="3"><circle cx="20" cy="14" r="8"/><circle cx="40" cy="14" r="8"/><path d="M6 40a14 12 0 0 1 28 0M26 40a14 12 0 0 1 28 0"/><path d="M4 46h52v8H4z"/></svg>
  <h3>Red Team<br>Adversary Simulation</h3>
  <p>A goal-based assessment where we attack just like a real world adversary. This includes external attacks and targeted phishing to demonstrate the real</p>
  <span class="more">READ MORE</span>
</div>
<div class="card" style="left:758px;top:1546px">
  <svg width="56" height="56" viewBox="0 0 56 56" fill="none" stroke="#ec1f27" stroke-width="3"><path d="M4 6h34v46H4z"/><path d="M10 16l3 3 5-5M10 30l3 3 5-5M22 17h10M22 31h10M10 42h22"/><path d="M46 8v36l4 6 4-6V8z"/></svg>
  <h3>Penetration Testing &amp;<br>Vulnerability Assessments</h3>
  <p>This includes vulnerability scans of the in-scope systems where we manually verify issues and exploit any issues found. We report on the issues that actually</p>
  <span class="more">READ MORE</span>
</div>
<div class="card" style="left:161px;top:1890px">
  <svg width="56" height="56" viewBox="0 0 56 56" fill="none" stroke="#ec1f27" stroke-width="3"><path d="M6 24h44v26H6z"/><circle cx="28" cy="14" r="9"/><path d="M28 2v4M28 22v4M16 14h4M36 14h4"/><path d="M14 34h28M14 42h20"/></svg>
  <h3>Advanced Product,<br>Hardware &amp; RF Testing</h3>
  <p>This is a highly customized assessment designed for you and your hardware. Depending on the product we will analyze custom RF protocols, reverse</p>
  <span class="more">READ MORE</span>
</div>
<div class="card" style="left:460px;top:1890px">
  <svg width="60" height="56" viewBox="0 0 60 56" fill="none" stroke="#ec1f27" stroke-width="3"><path d="M4 4h52v48H4zM4 14h52"/><path d="M12 24h14v16H12zM32 24h16M32 32h16M32 40h16"/></svg>
  <h3>Web Application<br>Penetration Testing</h3>
  <p>Our team will perform an in-depth analysis of your web application to find vulnerabilities related to programming errors, misconfiguration</p>
  <span class="more">READ MORE</span>
</div>
<div class="card" style="left:758px;top:1890px">
  <svg width="40" height="60" viewBox="0 0 40 60" fill="none" stroke="#ec1f27" stroke-width="3"><rect x="4" y="3" width="32" height="54" rx="4"/><path d="M4 48h32M13 20l14 14M27 20L13 34"/></svg>
  <h3>Mobile Application<br>Assessment</h3>
  <p>We look at your mobile application and the associated infrastructure to find configuration weaknesses, server-side issues, insecure authentication</p>
  <span class="more">READ MORE</span>
</div>

<h2 class="abs section-title about-title">ABOUT US</h2>
<div class="abs rule about-rule"></div>
<p class="abs lead about-lead">We focus on hacking. This is our passion. We find the vulnerabilities before the bad guys do.</p>
<div class="abs about-frame"></div>
<div class="abs about-image" role="img" aria-label="Screen reflected in a pair of glasses"></div>
<svg class="abs play" width="110" height="110" viewBox="0 0 110 110" fill="none" stroke="#fff" stroke-width="4"><circle cx="55" cy="55" r="50"/><polygon points="44,34 78,55 44,76"/></svg>

<svg class="abs testi-bg" viewBox="0 0 1200 660"><polygon points="0,60 380,0 1200,110 1200,660 0,660" fill="#f1f1f1"/></svg>
<h2 class="abs section-title testi-title">TESTIMONIALS</h2>
<div class="abs rule testi-rule"></div>

<div class="quote" style="left:79px;top:3288px">
  <p>" Our audit team found every point clearly mapped and the fixes easy to follow for our staff.</p>
  <div class="who"><div class="avatar" role="img" aria-label="Client portrait"></div><div><div class="who-name">Mara</div><div class="stars">★★★★★</div></div></div>
</div>
<div class="quote raised" style="left:436px">
  <p>I read the report yesterday. This is one of the best-written, actionable pentest reports I've ever seen.</p>
  <div class="who"><div class="avatar" role="img" aria-label="Client portrait" style="background:linear-gradient(#9ccc8a,#4f8a3c)"></div><div><div class="who-name">R.T (Undisclosed Organization)</div><div class="stars" style="color:#777">★★★★★</div></div></div>
</div>
<div class="quote" style="left:793px;top:3288px">
  <p>" A calm, thorough crew who explained each risk in plain terms and kept us informed throughout.</p>
  <div class="who"><div class="avatar" role="img" aria-label="Client portrait"></div><div><div class="who-name">Lena</div><div class="stars">★★★★★</div></div></div>
</div>

<svg class="abs footer" viewBox="0 0 1200 325"><polygon points="0,60 780,0 1200,90 1200,325 0,325" fill="#111214"/></svg>
<div class="abs foot-brand">
  <div class="brand-mark"></div>
  <div><div class="brand-name">BRASS LANTERN</div><div class="brand-tag">INFORMATION SECURITY</div></div>
</div>
<p class="abs foot-contact"><span>Email: contact@brasslantern.com</span><span>Phone: +1.555.014.2270</span></p>
<p class="abs foot-legal">© 2018 All rights are reserved. Privacy | Terms of use</p>
<div class="abs socials"><i></i><i></i><i></i><i></i></div>

</body>
</html>
```